Gum Care Season infographic - Bright Grins for Every Year

To create an infographic for Gum Care Season, August 2014, with the key messages of how the health of your mouth affects you through your lifetime.
We require two posters (A3 and A4 options) that will educate the Australian and New Zealand public of the importance of maintaining good oral health through facts and statistics (see attachments), focusing on different stages in your life.
The A3 poster will be used for: hanging in dental practices, posted in social media, on websites, advertising, public relations.
The A4 poster will be used for print handouts, websites, advertising, public relations.
Sections of the posters will be pulled out to be used in social media posts, on websites, in emails, etc.
Design constraints:
Poster One: Infographic Poster to be A3 (Appendix 1)
Poster Two: Infographic Poster to be reconfigured as A4 handout with limited facts (Appendix 2).
Full colour with the PVR colour palette reflected throughout.
Deliverables:
Design two infographics to reflect the tagline, Bright Grins for Every Year, and:
• One A3 poster to represents the key milestones as outlined in Appendix 1.
One A4 poster/handout to represent the key milestones in Appendix 2.
• Is obvious that these are stages in your life but does not mention the specific ages.
• Facts can be represented in icons, images, graphs, fractions, percentages, etc.
• Can be broken into smaller campaign sub messages.
• Includes: Gum Care Season and Bright Grins for Every Year text.
• Includes: A PVR Initiative logo.
• Includes August 2014 as Gum Care Season.
• Include website: www.pivoradental.example
• Is similar in style to the PVR launch infographic (attached).
• Clean, vibrant, understandable and friendly.
Tone:
PVR is experienced, reliable, caring, accessible, knowledgeable, friendly and confident in all aspects of dentistry.
The infographic can be ‘Tongue in cheek’ – friendly tone to suit different age groups through the messages, ie. 18-25 years is more conversational and cheeky, while 50+ could come from a ‘dad joke.’
See attached logo, colour palette and appendices.
Target Market(s)
Aussie and Kiwi families visiting a modern, bright, well-presented dental practice.
Industry/Entity Type
Health
Requirements
Must have
- Bright, clear and engaging. Needs to be suited to a professional dental practice, but also stand out on social media and in advertising.
Must have name of campaign and month, brand supporter, website - see brief.

```html
<!DOCTYPE html>
<html lang="en">
<head>
<meta charset="utf-8">
<title>Gum Care Season – Bright Grins for Every Year</title>
<link rel="stylesheet" href="https://fonts.googleapis.com/css2?family=Dosis:wght@400;500;600;700&display=swap">
<style>
  :root {
    --sky: #2bb5e8;
    --navy: #1c5d99;
    --deep-navy: #13467f;
    --sun: #fcc330;
    --white: #ffffff;
    --placeholder-sky: #5cc8ef;
  }
  * { margin: 0; padding: 0; box-sizing: border-box; }
  html, body { width: 1200px; height: 848px; overflow: hidden; }
  body { font-family: "Dosis", sans-serif; background: var(--sky); }
  .poster { position: relative; width: 1200px; height: 848px; background: var(--sky); overflow: hidden; }
  .shapes { position: absolute; inset: 0; }
  .txt { position: absolute; line-height: 1; }
  .masthead { left: 40px; top: 24px; font-size: 33px; font-weight: 500; color: var(--white); letter-spacing: 1px; white-space: nowrap; }
  .masthead .brand { font-weight: 700; font-size: 40px; margin: 0 8px; }
  .masthead .sep { margin: 0 12px; }
  .ribbon-label { font-size: 25px; font-weight: 500; color: var(--white); letter-spacing: 0.5px; white-space: nowrap; }
  .ribbon-label.on-sun { color: var(--navy); }
  .stat { font-weight: 500; color: var(--white); white-space: nowrap; }
  .stat.navy { color: var(--navy); }
  .stat.sun { color: var(--sun); }
  .note { font-size: 15px; font-weight: 500; color: var(--navy); line-height: 1.1; }
  .note.light { color: var(--white); font-size: 15px; }
  .placeholder { position: absolute; background: var(--placeholder-sky); border-radius: 6px; }
  .cost-box { position: absolute; left: 597px; top: 258px; width: 568px; height: 97px; background: var(--sun); border: 2px solid var(--white); outline: 4px solid var(--sun); }
  .cost-copy { left: 18px; top: 16px; font-size: 21px; font-weight: 500; color: var(--navy); line-height: 1.1; width: 270px; }
  .cost-figure { left: 285px; top: 12px; font-size: 66px; font-weight: 500; color: var(--navy); white-space: nowrap; }
  .fact-bar { font-size: 13.5px; font-weight: 600; line-height: 1.15; text-align: center; }
</style>
</head>
<body>
<main class="poster">
  <svg class="shapes" width="1200" height="848" viewBox="0 0 1200 848" aria-hidden="true">
    <polygon points="0,88 250,88 250,120 0,120" fill="var(--navy)"/>
    <polygon points="218,120 250,120 250,140" fill="var(--deep-navy)"/>
    <polygon points="250,106 620,106 595,123 620,140 250,140" fill="var(--sun)"/>
    <polygon points="0,312 305,312 305,345 0,345" fill="var(--navy)"/>
    <polygon points="300,322 365,322 340,340 365,358 300,358" fill="var(--deep-navy)"/>
    <polygon points="0,548 60,548 60,610 30,579" fill="var(--deep-navy)"/>
    <polygon points="480,548 560,548 530,579 560,610 480,610" fill="var(--deep-navy)"/>
    <rect x="18" y="566" width="512" height="56" fill="var(--navy)"/>
    <polygon points="700,100 800,100 800,140 700,140 725,120" fill="var(--deep-navy)"/>
    <rect x="795" y="85" width="405" height="34" fill="var(--navy)"/>
    <rect x="575" y="185" width="70" height="48" rx="3" fill="var(--navy)"/>
    <rect x="597" y="175" width="26" height="12" rx="2" fill="none" stroke="var(--navy)" stroke-width="4"/>
    <rect x="575" y="203" width="70" height="3" fill="var(--sky)"/>
    <rect x="606" y="199" width="8" height="10" fill="var(--sky)"/>
    <polygon points="690,400 790,400 790,440 690,440 715,420" fill="var(--deep-navy)"/>
    <rect x="785" y="380" width="415" height="32" fill="var(--navy)"/>
    <polygon points="555,690 640,612 745,612 745,625 640,690" fill="var(--deep-navy)"/>
    <rect x="740" y="590" width="460" height="33" fill="var(--navy)"/>
    <polygon points="555,690 895,690 910,712 895,735 555,735" fill="var(--navy)"/>
    <polygon points="905,690 1190,690 1190,735 1160,735 1160,760 905,760 905,735 920,712" fill="var(--sun)"/>
    <polygon points="505,760 905,760 890,780 905,800 505,800 520,780" fill="var(--sun)"/>
    <polygon points="905,760 1145,760 1145,805 890,805 875,782" fill="var(--navy)"/>
    <circle cx="435" cy="230" r="52" fill="none" stroke="var(--sun)" stroke-width="28"/>
    <path d="M 418.7 279.4 A 52 52 0 0 0 451.3 279.4" fill="none" stroke="var(--navy)" stroke-width="28"/>
    <circle cx="435" cy="230" r="36" fill="var(--sky)"/>
    <defs>
      <path id="donut-arc" d="M 359.4 200.5 A 81 81 0 1 0 510.6 200.5"/>
    </defs>
    <text font-family="Dosis, sans-serif" font-size="15" font-weight="500" fill="var(--navy)" letter-spacing="0.3">
      <textPath href="#donut-arc" startOffset="50%" text-anchor="middle">OF ALL DENTAL DISEASE IS PREVENTABLE</textPath>
    </text>
    <circle cx="480" cy="420" r="100" fill="var(--sun)"/>
    <path d="M 420 455 Q 480 510 540 455" fill="none" stroke="var(--navy)" stroke-width="9" stroke-linecap="round"/>
  </svg>

  <header class="txt masthead">A<span class="brand">PVR</span>INITIATIVE<span class="sep">|</span>AUGUST 2014 AS GUM CARE SEASON<span class="sep">|</span>pivoradental.example</header>

  <div class="txt ribbon-label" style="left:22px;top:92px;">GUM CARE SEASON</div>
  <div class="txt ribbon-label on-sun" style="left:266px;top:111px;">BRIGHT GRINS FOR EVERY YEAR</div>

  <div class="placeholder" style="left:38px;top:165px;width:150px;height:130px;" role="img" aria-label="Map of Australia in yellow and navy"></div>
  <div class="txt stat" style="left:190px;top:186px;font-size:52px;">30%</div>
  <div class="txt note light" style="left:190px;top:239px;">of Australians admit<br>they are only brushing<br>once daily</div>

  <div class="txt stat" style="left:405px;top:212px;font-size:34px;">90%</div>

  <div class="txt ribbon-label" style="left:46px;top:316px;">WATCH YOUR MOUTH!</div>

  <div class="placeholder" style="left:38px;top:370px;width:142px;height:160px;" role="img" aria-label="Pictograms of a woman and a man, half yellow half navy"></div>
  <div class="txt stat" style="left:190px;top:388px;font-size:78px;">50%</div>
  <div class="txt note light" style="left:193px;top:460px;">of 18–25 years old haven't<br>visited a dentist within past<br>12 months</div>

  <div class="txt stat navy" style="left:420px;top:352px;font-size:66px;">48%</div>
  <div class="txt note" style="left:405px;top:412px;width:150px;text-align:center;font-size:14.5px;">remember a smile on<br>first impression than<br>anything else</div>

  <div class="txt ribbon-label" style="left:18px;top:576px;width:512px;text-align:center;font-size:17px;line-height:1.1;">A QUARTER OF ALL ADULTS OVER THE AGE OF 15 REPORTED<br>THEY HAD FELT UNCOMFORTABLE ABOUT THEIR DENTAL APPEARANCE</div>

  <div class="txt stat navy" style="left:32px;top:672px;font-size:70px;">83%</div>
  <div class="txt note" style="left:35px;top:740px;font-size:14.5px;">say that decayed teeth<br>and bad breath are the<br>biggest turn offs on a<br>first date</div>

  <div class="placeholder" style="left:200px;top:645px;width:110px;height:190px;border-radius:30px 30px 20px 20px;background:#e8f6fc;" role="img" aria-label="White tooth with a navy decayed crown"></div>

  <div class="txt stat navy" style="left:348px;top:672px;font-size:70px;">50%</div>
  <div class="txt note" style="left:349px;top:742px;font-size:14.5px;">of Aussie kids now<br>suffer from this<br>preventable disease</div>

  <div class="txt ribbon-label" style="left:810px;top:89px;">WORKING ON IT!</div>

  <div class="txt stat sun" style="left:652px;top:170px;font-size:49px;">1 MILLION</div>
  <div class="txt note" style="left:654px;top:216px;">LOST DAYS OF WORK EACH YEAR</div>

  <div class="placeholder" style="left:868px;top:175px;width:30px;height:55px;background:var(--sun);border-radius:15px 15px 4px 4px;" role="img" aria-label="Ice cream cone icon"></div>
  <div class="txt note" style="left:908px;top:178px;font-size:15.5px;">APPROXIMATELY 17%<br>OF ADULTS AVOIDED EATING<br>CERTAIN FOODS BECAUSE OF PROBLEMS</div>

  <div class="cost-box">
    <div class="txt cost-copy">The total direct costs and lost productivity due to poor dental health in Australia is</div>
    <div class="txt cost-figure">$2 BILLON</div>
  </div>

  <div class="txt ribbon-label" style="left:800px;top:384px;">LIKE PULLING TEETH!</div>

  <div class="txt stat sun" style="left:658px;top:460px;font-size:68px;">600,000</div>
  <div class="txt note" style="left:660px;top:528px;font-size:21px;">DAYS LOST FROM SCHOOL</div>

  <div class="placeholder" style="left:895px;top:450px;width:22px;height:95px;background:var(--navy);transform:rotate(38deg);border-radius:3px;" role="img" aria-label="Navy pencil"></div>
  <div class="placeholder" style="left:960px;top:430px;width:190px;height:70px;background:var(--navy);border-radius:35px;" role="img" aria-label="Three child head silhouettes in caps, one yellow and two navy"></div>

  <div class="txt stat navy" style="left:928px;top:500px;font-size:66px;">68%</div>
  <div class="txt note" style="left:1052px;top:512px;font-size:14.5px;">of 2–5 year olds<br>have never visited<br>a dentist.</div>

  <div class="txt ribbon-label" style="left:755px;top:594px;">A GATEWAY TO HEALTH!</div>

  <div class="txt fact-bar" style="left:560px;top:696px;width:340px;color:var(--sun);">MORE THAN 90 PERCENT OF ALL SYSTEMIC DISEASES<br>— INCLUDING HEART DISEASE — HAVE ORAL SYMPTOMS</div>
  <div class="txt fact-bar" style="left:925px;top:696px;width:265px;color:var(--navy);">HALF OF PEOPLE AGED 45–64 ATTENDED<br>THE DENTIST BECAUSE OF A PROBLEM</div>
  <div class="txt fact-bar" style="left:515px;top:767px;width:380px;color:var(--navy);font-size:11.5px;">PEOPLE WITH PERIODONTAL DISEASE MAY BE MORE LIKELY TO HAVE<br>CORONARY ARTERY DISEASE THAN PEOPLE WITH HEALTHY MOUTHS.</div>
  <div class="txt fact-bar" style="left:935px;top:768px;width:200px;color:var(--sun);text-align:left;">53% OF 65 YEARS+ HAVE<br>PERIODONTAL DISEASE</div>
</main>
</body>
</html>
```